Vesk Architecture

We are a architectural design and build company working between scales 1/1000 to 1/1 we want people to understand our difference from our design experience and quality.we build hotels restourants and office spaces.Our company name is Vesk architecture to mind sustainability.

We want to write our adress phone and work spesifications on the card and we want our logo as backround.

Ps:you could find the logo adress and phone box numbers from the web:www.veskmimarlik-ornek.com

Target Market(s)

Who looks for experts.

Industry/Entity Type

Architecture

Requirements
Must have
• Design is over everything.
Should not have
• we don want it to be colorfull

```html
<!DOCTYPE html>
<html lang="tr">
<head>
<meta charset="utf-8">
<title>Vesk Architecture – Business Card</title>
<link rel="stylesheet" href="https://fonts.googleapis.com/css2?family=Carlito:wght@400;700&display=swap">
<style>
  :root {
    --stage: #0f4f63;
    --card-top: #ffffff;
    --card-bottom: #dcdcdc;
    --ink: #141414;
    --band: #2190de;
    --band-light: #3aa2ea;
    --rule: #2a8ad6;
    --faint: rgba(0, 0, 0, 0.07);
    --url: #444444;
    --stripe-a: #dbe8f4;
    --stripe-b: #f4f7fa;
  }
  * { box-sizing: border-box; margin: 0; padding: 0; }
  html, body {
    width: 1200px;
    height: 857px;
    overflow: hidden;
  }
  body {
    position: relative;
    background: var(--stage);
    font-family: "Carlito", "Calibri", sans-serif;
    color: var(--ink);
  }
  .card {
    position: absolute;
    width: 507px;
    height: 287px;
    border-radius: 4px;
    overflow: hidden;
    background: linear-gradient(135deg, var(--card-top) 0%, #f2f2f2 45%, var(--card-bottom) 100%);
    box-shadow: 0 6px 18px rgba(0, 0, 0, 0.35);
  }
  .card--front { left: 57px; top: 84px; }
  .card--back  { left: 641px; top: 376px; }

  .card__band {
    position: absolute;
    left: 0; right: 0; bottom: 0;
    height: 33px;
    background: linear-gradient(180deg, var(--band-light), var(--band));
  }
  .card__url {
    position: absolute;
    right: 72px;
    bottom: 38px;
    font-size: 8px;
    letter-spacing: 3px;
    color: var(--url);
  }
  .card--back .card__url { right: 6px; bottom: 40px; font-size: 10px; letter-spacing: 2.4px; }

  /* Front: name block */
  .wordmark {
    position: absolute;
    color: var(--ink);
    font-weight: 400;
    line-height: 1;
  }
  .wordmark__name { display: block; }
  .wordmark__sub { display: block; letter-spacing: 2px; }
  .card--front .wordmark { left: 112px; top: 20px; }
  .card--front .wordmark__name { font-size: 176px; letter-spacing: -2px; }
  .card--front .wordmark__sub { font-size: 36px; margin-top: -10px; padding-left: 6px; }

  /* Back */
  .corner-stripes {
    position: absolute;
    left: 0; top: 0;
    width: 135px; height: 115px;
    background: repeating-linear-gradient(135deg, var(--stripe-a) 0 6px, var(--stripe-b) 6px 14px);
    clip-path: polygon(0 0, 100% 0, 0 100%);
  }
  .card--back .wordmark { left: 22px; top: 8px; }
  .card--back .wordmark__name { font-size: 64px; letter-spacing: -1px; }
  .card--back .wordmark__sub { font-size: 14px; margin-top: -4px; padding-left: 2px; }

  .faint-mark {
    position: absolute;
    color: var(--faint);
    font-weight: 400;
    line-height: 1;
  }
  .faint-mark span { display: block; font-size: 11px; letter-spacing: 1px; }
  .faint-mark--1 { left: 148px; top: 20px; font-size: 40px; }
  .faint-mark--2 { left: 292px; top: 24px; font-size: 40px; }
  .faint-mark--3 { left: 16px; top: 140px; font-size: 40px; }
  .faint-mark--4 { left: 190px; top: 200px; font-size: 32px; }

  .contact-rule {
    position: absolute;
    left: 177px; top: 68px;
    width: 2px; height: 136px;
    background: var(--rule);
  }
  .contact {
    position: absolute;
    left: 199px; top: 81px;
    font-size: 14.5px;
    line-height: 18.4px;
    color: var(--ink);
    list-style: none;
    white-space: nowrap;
  }
  .contact__name { font-weight: 700; }
</style>
</head>
<body>

  <section class="card card--front" aria-label="Business card front">
    <div class="wordmark">
      <span class="wordmark__name">vesk</span>
      <span class="wordmark__sub">MİMARLIK</span>
    </div>
    <p class="card__url">www.veskmimarlik-ornek.com</p>
    <div class="card__band"></div>
  </section>

  <section class="card card--back" aria-label="Business card back">
    <div class="corner-stripes" role="img" aria-label="Light blue diagonal stripe ornament in the corner"></div>

    <div class="faint-mark faint-mark--1" aria-hidden="true">vesk<span>MİMARLIK</span></div>
    <div class="faint-mark faint-mark--2" aria-hidden="true">vesk<span>MİMARLIK</span></div>
    <div class="faint-mark faint-mark--3" aria-hidden="true">vesk<span>MİMARLIK</span></div>
    <div class="faint-mark faint-mark--4" aria-hidden="true">vesk<span>MİMARLIK</span></div>

    <div class="wordmark">
      <span class="wordmark__name">vesk</span>
      <span class="wordmark__sub">MİMARLIK</span>
    </div>

    <div class="contact-rule"></div>
    <ul class="contact">
      <li><span class="contact__name">Deniz Arman KAYA</span> - Mimar</li>
      <li>( Mimar - Architect )</li>
      <li>Yeniova Mah. Lale Cad. Defne Sok.</li>
      <li>No : 7 Kadiköy / ISTANBUL</li>
      <li>Telephone: 0216 555 01 40 , 0216 555 01 41</li>
      <li>Email;veskmimarlik@ornek-posta.com</li>
    </ul>

    <p class="card__url">www.veskmimarlik-ornek.com</p>
    <div class="card__band"></div>
  </section>

</body>
</html>
```